Green Logistics / Last Mile Delivery Firm needs cool one-page website

FYI - We do have a detailed brief in the uploaded files section below
COMPANY
We recently launched the company Brook Logistics which is a pioneer in urban green logistics and provides zero-emissions last mile delivery services (i.e. delivery of parcels with delivery vans to the doorstep of households) for its logistics and retail clients.
We take on urban parcel delivery for our clients with a 100% electric commercial vehicles fleet, fair and sustainable working conditions for our employees and an unparalleled professional and customer-focused mindset.
WEBSITE
In the detailed brief, we have provided examples to emulate. We need the design + coding of the website. Website needs to be friendly/optimized for and should open swiftly on both Android & iOS.
In general, the website should convey
- green mission of the company
- sustainability (good working conditions, focus on employees)
- customer orientation
- professionalism
DESIGN
In the detailed brief, we have provided designs to emulate.
Color design: we do have a logo which features 2 green colors (one lighter and one darker color tone). However, the colors on the website do not necessarily need to follow these 2 colors exactly as we are able to switch the logo colors.
Imagery: should reflect maybe 50% green/leaf/tree , 25% customer and employee orientation, and 25% logistics (here it's important that it is the last mile delivery, i.e. delivery with delivery vans to the doorstep of households)
Coding

```html
<!DOCTYPE html>
<html lang="en">
<head>
<meta charset="utf-8">
<title>Brook Logistics – Sustainable Last Mile</title>
<link href="https://fonts.googleapis.com/css2?family=Montserrat:wght@400;600;700;800;900&family=Lato:wght@400;700&display=swap" rel="stylesheet">
<style>
:root{
  --green:#2f9e44;
  --green-dark:#238636;
  --lime:#8cc63f;
  --lime-bright:#b3dc3c;
  --ink:#222;
  --text:#555;
  --grey-bg:#f3f3f3;
  --pale:#eef6dc;
  --red:#d9302c;
  --white:#fff;
}
*{box-sizing:border-box;margin:0;padding:0}
html,body{width:1200px;height:4906px;overflow:hidden}
body{font-family:"Lato",sans-serif;color:var(--text);background:var(--white);position:relative}
.sec{position:absolute;left:0;width:1200px}
.abs{position:absolute}
h1,h2,h3,h4,.mont{font-family:"Montserrat",sans-serif}
.kicker{font-family:"Montserrat",sans-serif;font-size:10px;letter-spacing:1px;color:var(--lime);text-transform:uppercase;text-align:center}
.sec-title{font-size:27px;font-weight:600;color:var(--ink);text-align:center;margin-top:6px}
.heart{display:block;margin:8px auto 0}

/* top bar */
.topbar{top:0;height:34px;background:var(--green);color:#fff;font-size:11px}
.topbar .contact{left:160px;top:10px;display:flex;gap:28px}
.topbar .social{right:160px;top:9px;display:flex;gap:8px}
.sq{width:16px;height:16px;background:rgba(255,255,255,.25);display:block}

/* nav */
.nav{top:34px;height:92px;background:#2d3230}
.brand{display:flex;align-items:center;gap:10px;font-family:"Montserrat",sans-serif;font-weight:700;font-size:15px;color:var(--lime)}
.brand .dot{width:34px;height:34px;border-radius:50%;background:var(--lime)}
.nav .brand{left:160px;top:27px}
.menu{left:440px;top:38px;display:flex;font-family:"Montserrat",sans-serif;font-size:12px;font-weight:600;color:#fff}
.menu span{padding:0 14px;border-left:1px solid #666}
.menu span:first-child{border:0;color:var(--lime);text-decoration:underline}
.lang{right:158px;top:34px;display:flex;gap:6px}
.lang span{font-size:9px;font-weight:700;color:#fff;padding:5px 8px;border:1px solid #777;display:flex;gap:4px;align-items:center}
.lang span:first-child{background:var(--lime);border-color:var(--lime)}
.lang i{width:10px;height:7px;background:#999;display:block}

/* hero */
.hero{top:126px;height:708px;background:linear-gradient(100deg,#3f8f3c 0%,#6aa85a 45%,#3c8a3a 75%,#2d7530 100%);overflow:hidden}
.hero .tag{left:165px;top:200px;font-family:"Montserrat",sans-serif;font-size:11px;letter-spacing:6px;color:#fff}
.hero h1{left:160px;top:222px;font-size:52px;font-weight:900;color:#fff;line-height:66px;letter-spacing:1px}
.hero h1 em{font-style:normal;color:var(--lime-bright)}
.hero p{left:164px;top:364px;width:700px;font-size:14px;line-height:25px;color:#fff}
.btn{display:inline-block;background:var(--lime);color:#fff;font-family:"Montserrat",sans-serif;font-size:11px;font-weight:700;text-transform:uppercase;text-align:center}
.hero .btn{left:160px;top:456px;width:128px;height:44px;line-height:44px}
.arrow{width:38px;height:38px;border-radius:50%;border:2px solid rgba(255,255,255,.8);background:rgba(255,255,255,.2)}
.hero .prev{left:78px;top:272px}.hero .next{left:1101px;top:272px}
.dots{left:551px;top:656px;display:flex;gap:8px}
.dots i{width:22px;height:3px;background:rgba(255,255,255,.5);display:block}
.dots i:nth-child(2){width:38px;background:#fff}
.van-label{right:6px;top:370px;font-family:"Montserrat",sans-serif;font-size:44px;line-height:54px;color:rgba(255,255,255,.45);font-weight:600}
.plant{left:140px;top:620px;width:170px;height:170px;border-radius:50%;background:radial-gradient(circle,#5aa33a,#2f7a2a 70%,transparent 72%);z-index:2}

/* about */
.about{top:834px;height:747px}
.about .head{left:0;top:76px;width:1200px}
.card{top:190px;width:271px;height:482px;background:#fff;box-shadow:0 2px 10px rgba(0,0,0,.1)}
.card .ph{height:206px}
.card .band{height:50px;margin:0 -9px;background:var(--lime);color:#fff;font-family:"Montserrat",sans-serif;font-size:14px;font-weight:600;text-align:center;line-height:50px}
.card.mid .band{background:var(--green)}
.card p{font-size:10.5px;line-height:22.5px;text-align:center;padding:20px 24px 0}

/* approach */
.approach{top:1581px;height:509px;background:var(--grey-bg);overflow:hidden}
.approach .head{left:0;top:70px;width:1200px}
.ground{left:0;bottom:0;width:1200px;height:120px;background:linear-gradient(90deg,#dedede 0%,#e8e8e8 45%,#b5d98b 55%,#8cc63f 100%)}
.tree{left:457px;top:200px;width:286px;height:309px;background:linear-gradient(90deg,#5b5b5b 0%,#8a8a8a 49.5%,#5aa33a 50.5%,#2f8a30 100%);clip-path:ellipse(50% 48% at 50% 45%)}
.list-l{left:100px;top:187px;width:308px;text-align:right}
.list-r{left:796px;top:187px;width:320px}
.list-l h4,.list-r h4{font-size:14.5px;font-weight:600;margin-bottom:20px}
.list-l h4{color:var(--red);text-decoration:line-through}
.list-r h4{color:var(--green)}
.list-l li,.list-r li{list-style:none;font-size:12.5px;line-height:31px}
.list-l li{color:var(--red);text-decoration:line-through}
.list-r li{color:var(--green)}

/* services */
.services{top:2090px;height:596px;background:#fff}
.services .head{left:0;top:72px;width:1200px}
.services .intro{left:160px;top:166px;width:880px;text-align:center;font-size:12.5px;line-height:23px}
.svc{top:238px;width:202px;height:286px}
.svc .ph{height:232px}
.svc .bar{height:54px;background:var(--green);color:#fff;font-family:"Montserrat",sans-serif;font-size:12px;font-weight:600;display:flex;justify-content:space-between;align-items:center;padding:0 18px}
.svc.feat{top:230px;height:304px;background:linear-gradient(160deg,#4aa84a,#2f9e44);box-shadow:0 8px 18px rgba(0,0,0,.2);padding:80px 22px;color:#fff;font-family:"Montserrat",sans-serif}
.svc.feat h4{font-size:13px;font-weight:700}
.svc.feat hr{width:22px;border:0;border-top:2px solid #fff;margin:14px 0}
.svc.feat p{font-size:11.5px;line-height:23px;font-weight:600}

/* touch */
.touch{top:2686px;height:228px;background:linear-gradient(90deg,#2f8a3a,#3d9a3f 55%,#2a7a33);color:#fff}
.touch h2{left:160px;top:68px;font-size:23px;font-weight:700}
.touch p{left:160px;top:112px;width:580px;font-size:12.5px;line-height:22px}
.touch .brand{left:650px;top:66px;color:#fff;font-size:10px}
.touch .brand .dot{width:24px;height:24px;background:#fff}
.touch .btn{left:911px;top:88px;width:127px;height:46px;line-height:46px}

/* careers */
.careers{top:2914px;height:591px}
.careers .pale{left:600px;top:0;width:600px;height:591px;background:var(--pale)}
.careers .photo{left:63px;top:63px;width:474px;height:362px;background:linear-gradient(135deg,#dfe3e3,#2f9e44 60%,#1f6f2b);border:8px solid #fff;box-shadow:0 3px 12px rgba(0,0,0,.25)}
.careers .head{left:600px;top:72px;width:600px}
.careers .body{left:659px;top:168px;width:480px}
.careers h3{font-size:17px;font-weight:500;color:var(--ink);margin-bottom:18px}
.careers h3 u{color:var(--green)}
.careers p{font-size:11.5px;line-height:22.5px;margin-bottom:11px}
.careers p.quote{color:var(--green);font-style:italic;font-weight:700;font-size:12.5px}
.accordion{margin-top:22px;height:40px;background:var(--lime);color:#fff;font-family:"Montserrat",sans-serif;font-size:11px;font-weight:700;display:flex;justify-content:space-between;align-items:center;padding:0 22px}

/* contact */
.contact{top:3505px;height:263px}
.contact .head{left:0;top:80px;width:1200px}
.contact .intro{left:160px;top:166px;width:880px;text-align:center;font-size:12.5px;line-height:22px}
.map{top:3768px;height:299px;background:linear-gradient(120deg,#eef0ee,#e3e8e4 40%,#d7e6d3 70%,#eceeec)}
.form{top:4067px;height:457px}
.info{left:181px;width:232px;height:96px;border:2px solid var(--lime)}
.info .ic{position:absolute;left:-21px;top:22px;width:38px;height:38px;background:var(--green);display:flex;align-items:center;justify-content:center}
.info h4{position:absolute;left:58px;top:30px;font-size:12px;font-weight:600;color:var(--ink)}
.info span{position:absolute;left:58px;top:50px;font-size:10px}
.field{border:1px solid #ddd;background:#fff;font-size:10px;color:#777;padding:11px 14px}
.send{left:461px;top:345px;width:206px;height:36px;line-height:36px}

/* footer */
.footer{top:4524px;height:324px;background:linear-gradient(180deg,#fafafa 0%,#f1f5ec 60%,#dbe9c9 100%)}
.footer .brand{left:160px;top:74px;color:var(--green);font-size:14px}
.footer .brand .dot{width:38px;height:38px}
.footer .about-t{left:160px;top:144px;width:200px;font-size:11px;line-height:22px}
.footer .ct{left:160px;top:240px;font-size:11px;line-height:26px}
.fcol{top:84px}
.fcol h4{font-size:15px;font-weight:600;color:var(--ink);margin-bottom:22px}
.fcol li{list-style:none;font-size:10.5px;line-height:30px;color:#444}
.fcol li b{color:var(--green);font-weight:400}
.fsoc{display:flex;gap:8px;margin-top:12px}
.fsoc i{width:28px;height:28px;background:#cfd6cc;display:block}
.fsoc i:nth-child(2){background:var(--green)}
.copy{top:4848px;height:58px;background:var(--green);color:#fff;text-align:center;font-size:12px;line-height:58px}
</style>
</head>
<body>

<header class="sec topbar">
  <div class="abs contact"><span>&#9742;&nbsp; 123 456 789 0</span><span>&#9993;&nbsp; info@example.com</span></div>
  <div class="abs social"><i class="sq"></i><i class="sq"></i><i class="sq"></i></div>
</header>

<nav class="sec nav">
  <div class="abs brand"><span class="dot"></span>Brook Logistics</div>
  <div class="abs menu"><span>HOME</span><span>ABOUT</span><span>SERVICES</span><span>CAREERS</span><span>CONTACT</span></div>
  <div class="abs lang"><span><i></i>EN</span><span><i></i>DE</span></div>
</nav>

<section class="sec hero" role="img" aria-label="Green electric delivery van driving through a city street">
  <div class="abs van-label">Zero<br>Emission<br>Vehicle</div>
  <div class="abs tag">BECAUSE WE CARE ABOUT TREES!</div>
  <h1 class="abs">BROOK LOGISTICS<br>SUSTAINABLE <em>LAST MILE!</em></h1>
  <p class="abs">Lorem Ipsum is simply dummy text of the printing and typesetting industry. Lorem Ipsum has been the industry's standard dummy text ever since the 1500s, when an unknown printer took a galley</p>
  <span class="abs btn">Get Started</span>
  <span class="abs arrow prev"></span><span class="abs arrow next"></span>
  <div class="abs dots"><i></i><i></i><i></i></div>
</section>
<div class="abs plant" style="top:740px" role="img" aria-label="Leafy green plant"></div>

<section class="sec about">
  <div class="abs head">
    <div class="kicker">Introduction</div>
    <h2 class="sec-title">About Us</h2>
    <svg class="heart" width="16" height="14" viewBox="0 0 16 14"><path d="M8 14L1.2 7A4 4 0 018 2a4 4 0 016.8 5z" fill="#8cc63f"/></svg>
  </div>
  <div class="abs card" style="left:158px">
    <div class="ph" role="img" aria-label="Warehouse workers in safety vests handling parcels" style="background:linear-gradient(135deg,#c9a476,#8b6a45 50%,#c8d84a)"></div>
    <div class="band">Who We Are</div>
    <p>Brook Logistics is a pioneer in urban green logistics and provides the zero-emissions last mile delivery services for its logistics and retail clients. We take on urban parcel delivery for our clients with a 100% electric commercial vehicles fleet, fair and sustainable working conditions for our employees and an unique professional customer-focused mindset.</p>
  </div>
  <div class="abs card mid" style="left:465px">
    <div class="ph" role="img" aria-label="Misty green forest" style="background:linear-gradient(180deg,#f1f3f1,#b9c9b8 50%,#2f6b37)"></div>
    <div class="band">Our Mission</div>
    <p>To satisfy consumers' ever-rising desire to buy products online, the CO2 emissions from the delivery traffic will increase by 32% in the top 100 cities globally until 2030. Our clients care about our planet the same way we do, which is why Brook Logistics helps make planet a better place by running the most environmentally friendly urban last mile possible.</p>
  </div>
  <div class="abs card" style="left:771px">
    <div class="ph" role="img" aria-label="White van with zero emissions lettering" style="background:linear-gradient(135deg,#f4f4f4,#dcdcdc 60%,#a8d05a)"></div>
    <div class="band">Our Values</div>
    <p>We see ourselves as a professional services company who strongly cares about the environment, clients &amp; customers, as well as its employees. We believe that delivering parcels with zero emissions and providing a unique customer experience through professional attitude and a great team spirit are the corner-stones for Brook Logistics to operate.</p>
  </div>
</section>

<section class="sec approach">
  <div class="abs ground" role="img" aria-label="Cracked dry ground turning into green grass"></div>
  <div class="abs tree" role="img" aria-label="Tree half bare and half in full green leaf"></div>
  <div class="abs head">
    <div class="kicker">Our Approach</div>
    <h2 class="sec-title">Brook Logistics Is:</h2>
    <svg class="heart" width="16" height="14" viewBox="0 0 16 14"><path d="M8 14L1.2 7A4 4 0 018 2a4 4 0 016.8 5z" fill="#8cc63f"/></svg>
  </div>
  <div class="abs list-l mont">
    <h4>An Ordinary Parcel Delivery Firm</h4>
    <ul><li>- Polluting our cities</li><li>- Always in a rush</li><li>- Short-term oriented</li><li>- Focusing on profit only</li><li>- Yet another parcel delivery firm</li></ul>
  </div>
  <div class="abs list-r mont">
    <h4>A pioneering Green Last Mile</h4>
    <ul><li>- Delivering parcels emissions-free</li><li>- Putting customer experience first</li><li>- Operating the business sustainably</li><li>- Environment, customers and employees</li><li>- A professional services company</li></ul>
  </div>
</section>

<section class="sec services">
  <div class="abs head">
    <div class="kicker">What We Offer</div>
    <h2 class="sec-title">Our Services</h2>
    <svg class="heart" width="16" height="14" viewBox="0 0 16 14"><path d="M8 14L1.2 7A4 4 0 018 2a4 4 0 016.8 5z" fill="#8cc63f"/></svg>
  </div>
  <p class="abs intro">Brook Logistics provides last mile delivery services in urban areas to clients in the logistics and retail space. Our permanent employees are all highly trained and commit to highest professional standards which we continuously review and further develop with them.</p>
  <div class="abs svc" style="left:160px">
    <div class="ph" role="img" aria-label="Green electric van on a wet road" style="background:linear-gradient(160deg,#9bb08a,#4e8a3a 55%,#5a5a5a)"></div>
    <div class="bar"><span>Zero-Emission Delivery</span><span>&uarr;</span></div>
  </div>
  <div class="abs svc feat" style="left:383px">
    <h4>Professional All Around</h4><hr>
    <p>We honor our commitments and hold ourselves to the very highest professional standards</p>
  </div>
  <div class="abs svc" style="left:610px">
    <div class="ph" role="img" aria-label="Courier in green uniform holding a parcel" style="background:linear-gradient(180deg,#f2f2f2,#2f9e44 60%,#c8a06a)"></div>
    <div class="bar"><span>Highly Trained Drivers</span><span>&uarr;</span></div>
  </div>
  <div class="abs svc" style="left:834px">
    <div class="ph" role="img" aria-label="Support agent with headset at a laptop" style="background:linear-gradient(180deg,#ececec,#c7b9a5 55%,#7a8a94)"></div>
    <div class="bar"><span>Rare Customer Focus</span><span>&uarr;</span></div>
  </div>
</section>

<section class="sec touch" role="img" aria-label="Green forest backdrop">
  <h2 class="abs">Get In Touch With Brook Logistics!</h2>
  <div class="abs brand"><span class="dot"></span>Brook Logistics</div>
  <p class="abs">If you got excited, or have a question about our services, our approach, our jobs or just want to get in touch to chat about how green logistics can make the planet a little bit better, please get in touch</p>
  <span class="abs btn">Contact Us</span>
</section>

<section class="sec careers">
  <div class="abs pale"></div>
  <div class="abs photo" role="img" aria-label="Smiling delivery driver in green cap giving a thumbs up from a van window"></div>
  <div class="abs head">
    <div class="kicker">Want To Join Us?</div>
    <h2 class="sec-title">Careers</h2>
    <svg class="heart" width="16" height="14" viewBox="0 0 16 14"><path d="M8 14L1.2 7A4 4 0 018 2a4 4 0 016.8 5z" fill="#8cc63f"/></svg>
  </div>
  <div class="abs body">
    <h3>IF YOU JOIN BROOK LOGISTICS, <u>YOU JOIN A FAMILY!</u></h3>
    <p>At the heart of everything we do at Brook Logistics is a relentless focus on our mission. That is why we aim to ensure that our employees can follow their own passion at the workplace, be this working in a truly collaborative and caring team, putting a smile on a customer's face or making the world a better place.</p>
    <p class="quote">"While we are helping our clients grow by delivering their parcels, we are also helping all of our employees grow personally and professionally."</p>
    <p>We care about our employees' happiness and well being which is why we are providing additional benefits like the supplementary health insurance. If you are excited about joining our Brook Logistics family, please check out our open positions.</p>
    <div class="accordion"><span>FULL-TIME DRIVER / PARCEL DELIVERER</span><span>+</span></div>
  </div>
</section>

<section class="sec contact">
  <div class="abs head">
    <div class="kicker">We'd Love To Hear From You!</div>
    <h2 class="sec-title">Contact Us</h2>
    <svg class="heart" width="16" height="14" viewBox="0 0 16 14"><path d="M8 14L1.2 7A4 4 0 018 2a4 4 0 016.8 5z" fill="#8cc63f"/></svg>
  </div>
  <p class="abs intro">Whether you have a question about our services, our approach, our jobs or just want to get in touch to chat about how green logistics can make the planet a little bit better, our team is ready to answer your questions and enquiries.</p>
</section>

<div class="sec map" role="img" aria-label="City street map showing the office location"></div>

<section class="sec form">
  <div class="abs info" style="top:61px"><div class="ic"><svg width="18" height="14" viewBox="0 0 18 14" fill="none" stroke="#fff" stroke-width="1.5"><rect x="1" y="1" width="16" height="12"/><path d="M1 1l8 7 8-7"/></svg></div><h4>Where To Email Us:</h4><span>email@example.com</span></div>
  <div class="abs info" style="top:175px"><div class="ic"><svg width="16" height="16" viewBox="0 0 16 16" fill="none" stroke="#fff" stroke-width="1.5"><path d="M3 1l3 3-2 2c1 2 3 4 5 5l2-2 3 3-2 2C7 14 2 9 1 3z"/></svg></div><h4>Where To Call Us:</h4><span>012 - 345 - 6789</span></div>
  <div class="abs info" style="top:290px"><div class="ic"><svg width="14" height="18" viewBox="0 0 14 18" fill="none" stroke="#fff" stroke-width="1.5"><path d="M7 17S1 10 1 6.5a6 6 0 0112 0C13 10 7 17 7 17z"/><circle cx="7" cy="6.5" r="2"/></svg></div><h4>Where To Find Us:</h4><span>text filler for design purpose</span></div>
  <div class="abs field" style="left:461px;top:61px;width:278px;height:35px">Full Name*</div>
  <div class="abs field" style="left:762px;top:61px;width:278px;height:35px">Email Address*</div>
  <div class="abs field" style="left:461px;top:118px;width:278px;height:35px">Phone Number*</div>
  <div class="abs field" style="left:762px;top:118px;width:278px;height:35px">Subject*</div>
  <div class="abs field" style="left:461px;top:174px;width:579px;height:148px">Type your message here...</div>
  <span class="abs btn send">Send Message</span>
</section>

<footer class="sec footer">
  <div class="abs brand"><span class="dot"></span>Brook Logistics</div>
  <p class="abs about-t">Some text filler here that has been used for design purposes, in order to fill and avoid the empty spaces.</p>
  <div class="abs ct">&#9742;&nbsp; 012 345 6789<br>&#9993;&nbsp; info@example.com</div>
  <div class="abs fcol" style="left:446px"><h4>Quick Links</h4><ul><li><b>&gt;&gt; Home</b></li><li>&gt;&gt; About Us</li><li>&gt;&gt; Services</li><li>&gt;&gt; Careers</li><li>&gt;&gt; Contact</li></ul></div>
  <div class="abs fcol" style="left:680px"><h4>Information</h4><ul><li>&gt;&gt; Privacy Policy</li><li>&gt;&gt; Legal Notice</li></ul></div>
  <div class="abs fcol" style="left:892px"><h4>Find Us At</h4><ul><li>-Follow Us On Socials Media:</li></ul><div class="fsoc"><i></i><i></i><i></i></div></div>
</footer>

<div class="sec copy">Copyright &copy; 2020 <b>Brook Logistics</b> - All Rights Reserved</div>

</body>
</html>
```